Ecommerce Website For Printing Company

Zoravquill.com are a print, design and signage company who sell flyers, business cards, posters, brochures and more to customers in the UK.

Our website is outdated and requires a new design using current web styling and mobile functionality.

We require the following pages to be designed;
- Home Page
- Price Page
- Portfolio Page
- Blog
- Content Page

Our competitors in the printing industry are www.brenticade.com, www.hallowmarsh.co.uk, quorelvane.co.uk, www.tambridok.co.uk

We require the website to give a professional image as well as be easy for customers to navigate, understand and find prices.

Target Market(s)

Businesses

Industry/Entity Type

Printing

Number of Pages Required

4 page

Font styles to use
Sans Serif

Colors
33a6d7

Requirements
Must have
• Popular products, latest news/blog, sales from portfolio, newsletter sign up, footer

```html
<!DOCTYPE html>
<html lang="en">
<head>
<meta charset="utf-8">
<title>Zoravquill.com – Print, Design &amp; Signage</title>
<link href="https://fonts.googleapis.com/css2?family=Roboto+Condensed:wght@400;700&family=Open+Sans:wght@400;600;700&display=swap" rel="stylesheet">
<style>
:root{
  --brand:#33a6d7;
  --teal:#3fc3cc;
  --teal-dark:#1fa3b0;
  --navy:#0c2a4a;
  --navy-2:#113a63;
  --ink:#2f3a44;
  --muted:#7a8791;
  --grey-bg:#eceff1;
  --yellow:#f4b71a;
  --white:#ffffff;
  --line:#d6dde2;
}
*{box-sizing:border-box;margin:0;padding:0}
html,body{width:1200px;height:4052px;overflow:hidden}
body{font-family:"Open Sans",Arial,sans-serif;color:var(--ink);background:var(--white);font-size:13px}
.wrap{width:1000px;margin:0 auto;position:relative}

/* hero */
.hero{position:relative;height:560px;background:linear-gradient(180deg,#8a8f93 0%,#6d7378 55%,#3e5d73 100%)}
.hero-photo{position:absolute;inset:0;background:linear-gradient(120deg,#9aa3a8,#5f6a72 50%,#7b8a95)}
.hero-tint{position:absolute;left:0;right:0;bottom:0;height:230px;background:linear-gradient(180deg,rgba(51,166,215,0) 0%,rgba(51,166,215,.55) 100%)}
.topbar{position:absolute;top:0;left:100px;width:1000px;height:62px;background:var(--white);display:flex;align-items:center;padding:0 18px}
.logo{display:flex;align-items:center;gap:8px;font-family:"Roboto Condensed",sans-serif;font-weight:700;font-size:24px;color:var(--navy)}
.logo i{width:22px;height:22px;background:var(--brand);display:block}
.top-contact{margin-left:70px;font-size:11px;line-height:15px;color:var(--ink)}
.top-contact b{font-size:15px;color:var(--navy)}
.top-btns{margin-left:auto;display:flex;gap:6px}
.top-btns span{background:var(--navy);color:var(--white);font-size:10px;font-weight:700;padding:6px 10px;text-transform:uppercase}
.top-btns span.alt{background:var(--brand)}
.nav{position:absolute;top:62px;left:100px;width:1000px;height:34px;background:var(--navy);display:flex;align-items:center;padding:0 18px;gap:18px}
.nav a{color:var(--white);text-decoration:none;font-family:"Roboto Condensed",sans-serif;font-size:12px;font-weight:700;text-transform:uppercase}
.hero-copy{position:absolute;left:0;right:0;top:398px;text-align:center;color:var(--white);font-family:"Roboto Condensed",sans-serif;text-transform:uppercase}
.hero-copy h1{font-size:38px;line-height:40px;font-weight:700}
.hero-copy p{font-size:28px;line-height:32px;font-weight:700}
.hero-copy small{display:block;font-size:22px;margin-top:4px;font-weight:400;opacity:.8}

/* feature boxes */
.features{background:linear-gradient(180deg,#6fc4df 0%,#d4eef5 100%);height:320px}
.features .wrap{display:flex;gap:10px;justify-content:center;position:relative;top:-6px}
.feature{width:282px;background:var(--navy-2);color:var(--white)}
.feature-img{height:110px;background:linear-gradient(135deg,#c9d6de,#8fa8b8)}
.feature-body{padding:12px 14px 14px;background:var(--brand);height:178px}
.feature:nth-child(2) .feature-body{background:var(--navy-2)}
.feature:nth-child(3) .feature-body{background:#1b8fc4}
.feature h3{font-family:"Roboto Condensed",sans-serif;font-size:20px;line-height:21px;text-transform:uppercase;font-weight:700}
.feature p{font-size:11px;line-height:16px;margin:8px 0 12px;opacity:.9}
.btn-y{display:inline-block;background:var(--yellow);color:var(--navy);font-size:10px;font-weight:700;text-transform:uppercase;padding:6px 12px}

/* intro */
.intro{height:300px;background:linear-gradient(180deg,#d4eef5 0%,#ffffff 60%);overflow:hidden}
.intro .wrap{display:flex;gap:30px;padding:40px 100px 0 130px;align-items:flex-start}
.intro-tag{flex:0 0 270px;font-family:"Roboto Condensed",sans-serif;font-weight:700;font-size:42px;line-height:42px;color:var(--brand);text-transform:uppercase;white-space:nowrap}
.intro-tag span{color:var(--teal-dark)}
.intro-text{flex:1 1 auto;padding-top:4px}
.intro-text h2{font-family:"Roboto Condensed",sans-serif;font-size:26px;color:var(--navy);text-transform:uppercase}
.intro-text p{font-size:12px;line-height:19px;margin-top:8px;color:var(--ink)}

/* products */
.section-title{font-family:"Roboto Condensed",sans-serif;font-weight:700;text-transform:uppercase;font-size:22px;color:var(--navy);padding:28px 0 22px 0}
.products{background:var(--grey-bg);height:720px}
.grid{display:grid;grid-template-columns:repeat(4,180px);gap:28px 16px;margin-left:130px}
.card{background:var(--white);border:1px solid var(--line);text-align:center;padding-bottom:10px}
.card-img{height:120px;background:linear-gradient(135deg,#dfe8ec,#a9c3cf)}
.card-name{background:var(--white);color:var(--navy);font-family:"Roboto Condensed",sans-serif;font-weight:700;font-size:14px;text-transform:uppercase;padding:8px 0 2px}
.card-from{font-size:10px;color:var(--muted)}
.card-price{font-family:"Roboto Condensed",sans-serif;font-size:28px;color:var(--teal-dark);line-height:32px}
.card-btn{display:inline-block;border:1px solid var(--brand);color:var(--brand);font-size:10px;font-weight:700;text-transform:uppercase;padding:4px 12px;margin-top:4px}

.large{background:linear-gradient(180deg,var(--teal) 0%,#7fd6dd 100%);height:400px}
.large .section-title{color:var(--white)}

/* testimonial */
.testimonial{background:linear-gradient(135deg,#0b2544,#12406b 60%,#0b2544);height:320px;text-align:center;color:var(--white);padding-top:40px}
.avatar{width:100px;height:100px;border-radius:50%;border:4px solid var(--white);margin:0 auto;background:linear-gradient(180deg,#b9c4cc,#6c7b86)}
.t-name{font-family:"Roboto Condensed",sans-serif;font-weight:700;font-size:14px;text-transform:uppercase;margin-top:12px}
.t-role{font-size:10px;opacity:.7;text-transform:uppercase}
.t-quote{width:560px;margin:14px auto 0;font-size:12px;line-height:19px;font-style:italic;opacity:.9}
.dots{margin-top:16px;display:flex;justify-content:center;gap:6px}
.dots i{width:8px;height:8px;border-radius:50%;background:rgba(255,255,255,.45);display:block}
.dots i.on{background:var(--white)}

/* portfolio */
.portfolio{height:500px;text-align:center;padding-top:30px}
.portfolio h2{font-family:"Roboto Condensed",sans-serif;text-transform:uppercase;color:var(--navy);line-height:1}
.portfolio h2 small{display:block;font-size:22px}
.portfolio h2 span{font-size:54px;color:var(--brand)}
.portfolio p.lead{width:600px;margin:12px auto 26px;font-size:12px;line-height:18px;color:var(--muted)}
.portfolio .grid{text-align:left}
.portfolio .card{text-align:left;border:none}
.portfolio .card-img{height:170px}
.portfolio .card-name{padding:8px 0 4px;font-size:13px}
.portfolio .card-btn{margin-top:0}

/* partners */
.partners{height:280px;background:var(--grey-bg);text-align:center;padding-top:26px}
.partners h3{font-family:"Roboto Condensed",sans-serif;color:var(--teal-dark);font-size:26px;font-weight:700}
.partner-row{display:flex;justify-content:center;gap:70px;margin-top:30px;align-items:center}
.partner-row span{font-family:"Open Sans",sans-serif;font-weight:700;font-size:24px;color:var(--navy)}
.stats{display:flex;justify-content:center;gap:110px;margin-top:40px}
.stat b{display:block;font-family:"Roboto Condensed",sans-serif;font-size:28px;color:var(--navy)}
.stat span{font-size:10px;color:var(--muted);text-transform:uppercase}

/* quick links */
.quick{height:340px;position:relative;background:linear-gradient(90deg,#4d5f6c,#2d3f4e 40%,#4e6270)}
.quick-panel{position:absolute;left:260px;width:680px;top:0;height:340px;background:rgba(10,36,64,.92);color:var(--white);padding:26px 30px}
.quick-panel h3{font-family:"Roboto Condensed",sans-serif;text-transform:uppercase;font-size:24px;text-align:center}
.quick-panel p.sub{font-size:10px;text-align:center;opacity:.7;margin-top:2px}
.links{display:grid;grid-template-columns:repeat(4,1fr);gap:10px;margin-top:22px}
.links ul{list-style:none}
.links li{font-size:11px;line-height:21px;opacity:.85}

/* help */
.help{height:200px;background:var(--white);text-align:center;padding-top:20px}
.help h3{font-family:"Roboto Condensed",sans-serif;font-size:24px;color:var(--navy)}
.help p{font-size:11px;color:var(--muted);margin-top:2px}
.cta-row{display:flex;justify-content:center;gap:8px;margin-top:18px}
.cta{width:220px;height:92px;text-align:left;padding:18px 16px;color:var(--white);font-family:"Roboto Condensed",sans-serif;text-transform:uppercase}
.cta small{display:block;font-size:11px;opacity:.85}
.cta b{font-size:22px;line-height:24px}
.cta.up{background:var(--brand)}
.cta.news{background:var(--navy-2)}
.cta.blog{background:var(--yellow);color:var(--navy)}

/* footer */
.footer{height:112px;background:var(--grey-bg);text-align:center;padding-top:12px}
.social{display:flex;justify-content:center;gap:8px}
.social i{width:28px;height:28px;border-radius:50%;background:var(--brand);display:block}
.foot-nav{margin-top:10px;display:flex;justify-content:center;gap:14px}
.foot-nav a{font-size:10px;font-weight:700;color:var(--navy);text-decoration:none;text-transform:uppercase}
.foot-logo{margin-top:8px;font-family:"Roboto Condensed",sans-serif;font-weight:700;font-size:18px;color:var(--navy)}
.foot-legal{font-size:9px;color:var(--muted);margin-top:2px}
</style>
</head>
<body>

<header class="hero">
  <div class="hero-photo" role="img" aria-label="Photo of three businessmen reviewing printed material in a print shop"></div>
  <div class="hero-tint"></div>
  <div class="topbar">
    <div class="logo"><i></i>Zoravquill</div>
    <div class="top-contact">Call now and order today<br><b>01632 960 418</b></div>
    <div class="top-btns"><span>Register</span><span>Sign in</span><span class="alt">Upload artwork</span></div>
  </div>
  <nav class="nav">
    <a href="#">Company</a><a href="#">Printing</a><a href="#">Graphic design</a><a href="#">Website design</a><a href="#">Artwork guide</a><a href="#">Pricing &amp; file</a><a href="#">Testimonials</a><a href="#">Blog</a><a href="#">Contact us</a>
  </nav>
  <div class="hero-copy">
    <h1>We'd like to print for you.</h1>
    <p>Low printing prices on hi-definition printing</p>
    <small>Professional quality for your business</small>
  </div>
</header>

<section class="features">
  <div class="wrap">
    <div class="feature">
      <div class="feature-img" role="img" aria-label="Photo of a designer working with colour swatches"></div>
      <div class="feature-body"><h3>In house<br>design team</h3><p>Our friendly designers create artwork for flyers, cards and brochures that make your brand stand out.</p><span class="btn-y">Find out more</span></div>
    </div>
    <div class="feature">
      <div class="feature-img" role="img" aria-label="Photo of printed colour samples"></div>
      <div class="feature-body"><h3>Our products<br>&amp; prices</h3><p>Browse our full range of print products with clear prices and fast turnaround on every order.</p><span class="btn-y">View all products</span></div>
    </div>
    <div class="feature">
      <div class="feature-img" role="img" aria-label="Photo of boxed print orders ready for delivery"></div>
      <div class="feature-body"><h3>Our free<br>delivery promise</h3><p>Every order ships free to any UK address, tracked and delivered right to your door.</p><span class="btn-y">Find out more</span></div>
    </div>
  </div>
</section>

<section class="intro">
  <div class="wrap">
    <div class="intro-tag">Small enough<br>to care.<br><span>Big enough<br>to cope.</span></div>
    <div class="intro-text">
      <h2>Welcome to Zoravquill</h2>
      <p><b>Zoravquill.com</b> is a local printing and design company working on a national level serving businesses and organisations all over the United Kingdom and Europe. As a company we are small enough to care and big enough to cope. We are a private limited company based at the heart of a franchise. Our office is based in County Durham in the North East of England.</p>
    </div>
  </div>
</section>

<section class="products">
  <div class="wrap">
    <h2 class="section-title">Select some of our popular products</h2>
    <div class="grid">
      <div class="card"><div class="card-img" role="img" aria-label="Photo of printed flyers"></div><div class="card-name">Flyer printing</div><div class="card-from">from</div><div class="card-price">£29</div><span class="card-btn">Shop now</span></div>
      <div class="card"><div class="card-img" role="img" aria-label="Photo of folded flyers"></div><div class="card-name">Folded flyers</div><div class="card-from">from</div><div class="card-price">£31</div><span class="card-btn">Shop now</span></div>
      <div class="card"><div class="card-img" role="img" aria-label="Photo of printed brochures"></div><div class="card-name">Brochure printing</div><div class="card-from">from</div><div class="card-price">£56</div><span class="card-btn">Shop now</span></div>
      <div class="card"><div class="card-img" role="img" aria-label="Photo of printed posters"></div><div class="card-name">Poster printing</div><div class="card-from">from</div><div class="card-price">£28</div><span class="card-btn">Shop now</span></div>
      <div class="card"><div class="card-img" role="img" aria-label="Photo of business cards"></div><div class="card-name">Business cards</div><div class="card-from">from</div><div class="card-price">£16</div><span class="card-btn">Shop now</span></div>
      <div class="card"><div class="card-img" role="img" aria-label="Photo of letterheads"></div><div class="card-name">Letterhead printing</div><div class="card-from">from</div><div class="card-price">£36</div><span class="card-btn">Shop now</span></div>
      <div class="card"><div class="card-img" role="img" aria-label="Photo of compliment slips"></div><div class="card-name">Compliment slips</div><div class="card-from">from</div><div class="card-price">£40</div><span class="card-btn">Shop now</span></div>
      <div class="card"><div class="card-img" role="img" aria-label="Photo of roll-up banners"></div><div class="card-name">Rollup banners</div><div class="card-from">from</div><div class="card-price">£79</div><span class="card-btn">Shop now</span></div>
    </div>
  </div>
</section>

<section class="large">
  <div class="wrap">
    <h2 class="section-title">Large format</h2>
    <div class="grid">
      <div class="card"><div class="card-img" role="img" aria-label="Photo of mesh banner print"></div><div class="card-name">Mesh</div><div class="card-from">from</div><div class="card-price">£35</div><span class="card-btn">Shop now</span></div>
      <div class="card"><div class="card-img" role="img" aria-label="Photo of backlit film print"></div><div class="card-name">Backlit film</div><div class="card-from">from</div><div class="card-price">£31</div><span class="card-btn">Shop now</span></div>
      <div class="card"><div class="card-img" role="img" aria-label="Photo of rigid sign board"></div><div class="card-name">Rigid sign boards</div><div class="card-from">from</div><div class="card-price">£56</div><span class="card-btn">Shop now</span></div>
      <div class="card"><div class="card-img" role="img" aria-label="Photo of PVC vinyl banner"></div><div class="card-name">PVC vinyl</div><div class="card-from">from</div><div class="card-price">£28</div><span class="card-btn">Shop now</span></div>
    </div>
  </div>
</section>

<section class="testimonial">
  <div class="avatar" role="img" aria-label="Portrait of the reviewing customer"></div>
  <div class="t-name">Corwin Ashdale</div>
  <div class="t-role">Managing director</div>
  <p class="t-quote">"Lovely service from start to finish, helpful staff, fair prices and great quality. Our flyers arrived ahead of schedule and looked better than we hoped. We will be back for our next campaign."</p>
  <div class="dots"><i class="on"></i><i></i><i></i><i></i><i></i></div>
</section>

<section class="portfolio">
  <h2><small>Wide range of</small><span>Portfolio</span></h2>
  <p class="lead">We offer a range of creative services for any business and budget. If you have a print job in mind, our designers and printers are ready to help. Take a look at some recent work.</p>
  <div class="wrap">
    <div class="grid">
      <div class="card"><div class="card-img" role="img" aria-label="Flyer design sample"></div><div class="card-name">Flyer design</div><span class="card-btn">View more</span></div>
      <div class="card"><div class="card-img" role="img" aria-label="Brochure design sample"></div><div class="card-name">Brochure design</div><span class="card-btn">View more</span></div>
      <div class="card"><div class="card-img" role="img" aria-label="Web design sample"></div><div class="card-name">Web design</div><span class="card-btn">View more</span></div>
      <div class="card"><div class="card-img" role="img" aria-label="Business card design sample"></div><div class="card-name">Business card</div><span class="card-btn">View more</span></div>
    </div>
  </div>
</section>

<section class="partners">
  <h3>Some of the companies we've good relationship over the years.</h3>
  <div class="partner-row"><span>Brallow</span><span>Quintelo</span><span>Marrowgate</span><span>Tessaly</span><span>Ondrafield</span></div>
  <div class="stats">
    <div class="stat"><b>50+</b><span>Team members</span></div>
    <div class="stat"><b>260+</b><span>Print products</span></div>
    <div class="stat"><b>7,500+</b><span>Happy customers</span></div>
    <div class="stat"><b>25,000+</b><span>Orders delivered</span></div>
  </div>
</section>

<section class="quick" role="img" aria-label="Photo of people around a table reviewing print samples">
  <div class="quick-panel">
    <h3>Quick printing products links</h3>
    <p class="sub">We have a wide range of printing options for you to choose from</p>
    <div class="links">
      <ul><li>Flyer printing</li><li>Folded flyers</li><li>Brochure printing</li><li>Poster printing</li><li>Business cards</li><li>Letterhead printing</li></ul>
      <ul><li>Rollup banners</li><li>Outdoor banners</li><li>Stickers and labels</li><li>Compliment slips</li><li>Presentation folders</li><li>Booklets</li></ul>
      <ul><li>Mesh banners</li><li>Backlit film</li><li>Sign boards</li><li>PVC vinyl</li><li>Window graphics</li><li>Vehicle graphics</li></ul>
      <ul><li>Flyer design</li><li>Brochure design</li><li>Logo design</li><li>Web design</li><li>Artwork checks</li><li>Templates</li></ul>
    </div>
  </div>
</section>

<section class="help">
  <h3>Need help or advice?</h3>
  <p>Call us now on 01632 960 418 or email info@zoravquill.com</p>
  <div class="cta-row">
    <div class="cta up"><small>Start your print</small><b>Upload your file</b></div>
    <div class="cta news"><small>Get special offers &amp; discounts</small><b>Newsletter</b></div>
    <div class="cta blog"><small>Print tips &amp; news</small><b>Blog &amp; news</b></div>
  </div>
</section>

<footer class="footer">
  <div class="social"><i></i><i></i><i></i><i></i></div>
  <div class="foot-nav"><a href="#">Company</a><a href="#">Printing</a><a href="#">Graphic design</a><a href="#">Website design</a><a href="#">Artwork guide</a><a href="#">Blog</a><a href="#">Contact us</a></div>
  <div class="foot-logo">Zoravquill</div>
  <div class="foot-legal">© Zoravquill.com. All rights reserved. Terms &amp; conditions · Privacy policy</div>
</footer>

</body>
</html>
```